Pale Lantern Double Sided Flyer Design

We need a double sided flyer (1/3 of an A4 which is 99mm x 210mm) developed for our Newcastle(NSW) tour. This flyer will be placed in tourist information centres and hotels. We want it to direct people to our website or be able to make bookings over the phone.

About Us:-
We are a city walking tour company that runs tours day or night. We run both day and night and will incorporate real history / real Pale lantern. Some of the stories will be quite serious i.e.- there are infamous murders from 100 years ago, baffling court cases, even a bit of poetry written by murderers, suicides, love triangles, you name it. We will be telling the historical stories that tourists will not hear from any other tour provider. A bit of darkness, a bit of mystery and a bit of history theme.

We do no go for scares and let the very real stories deliver the entertainment for our guests. Our customers enjoy our tours, but it isn't light fun and frivolity. Our stories are being carefully crafted and are packed with unexpected twists, turns; revelations whilst remaining all 100% true. We deliver deep, rich, engaging stories.

Here are a few samples of quotes from the characters in our stories that may give you an idea of the kind of history we will cover:-

"There were bits of spines, bits of skulls, [and] finger bones spilled out all over the streets - I ended up filling three boxes. Children were playing with them for weeks”

"I had a close shave last night and now I want a close haircut.”

“She's a beautiful child', isn't she? She's the cause of all the trouble.”

“I did it because she would not come home with me.”

"I have killed my wife. I’m glad she’s dead.”

"Stand aside or I'll put a bullet through both of you."

“You villain, I'll teach you to take away my character."

“You’re not dead yet, you bastard!”

Our website, booking form and contact details can be viewed at www.palelantern.com.au

Target Market(s)

Tourists

Industry/Entity Type

Tour

Colors

Designer to choose colors to be used in the design.

Requirements
Must have
• Vertical orientation please.
• Please also include a reference to a discount offer of 25% using the promo code "WICK".
Nice to have
• FRONT FLYER INFORMATION
• - Pale Lantern Logo
• - "I have killed my wife; I'm glad she's dead."
• - Harbourside Hidden Lanes Walk
• - 25% Discount Offer Codeword WICK
• - web address at the base; www.palelantern.com.au
• BACK FLYER INFORMATION
• - "She's a beautiful child', isn't she? She's the cause of all the trouble.
• - Pale Lantern Logo at the base along with the web address www.palelantern.com.au
• - Blurb:- Pale lantern brings back Newcastle's hidden past, the forgotten past, the dark past that may not want to be remembered.
• Real stories from the streets around you. Discover the histories you won't hear anywhere else. The forgotten stories of yesteryear finally get a chance to be told. Through you they get to live again.
Should not have
• GENERAL
• Please do not include the phone number, email address or social media icons. We want to drive online bookings.

```html
<!DOCTYPE html>
<html lang="en">
<head>
<meta charset="utf-8">
<title>Pale Lantern – Two Sided Flyer</title>
<link rel="stylesheet" href="https://fonts.googleapis.com/css2?family=Tinos:wght@400;700&display=swap">
<style>
  :root {
    --sheet: #0a0a0a;
    --sheet-glow: #1e1e1e;
    --cream: #f3e4b8;
    --gold-line: #b89a5e;
    --crimson: #5c0e0e;
    --crimson-deep: #2a0404;
    --crimson-mid: #3f0808;
    --photo-dark: #151515;
    --photo-light: #6e6e6e;
  }
  * { margin: 0; padding: 0; box-sizing: border-box; }
  html, body { width: 1200px; height: 821px; overflow: hidden; }
  body {
    position: relative;
    background: var(--sheet);
    font-family: "Tinos", "Times New Roman", serif;
    color: var(--cream);
  }
  .backdrop-city {
    position: absolute; inset: 0;
    background: radial-gradient(ellipse at 75% 50%, var(--sheet-glow) 0%, var(--sheet) 70%);
  }
  .side-label {
    position: absolute; font-size: 39px; line-height: 44px; text-align: center; width: 200px;
  }
  .label-back { left: 449px; top: 96px; }
  .label-front { left: 130px; top: 694px; }

  .flyer {
    position: absolute;
    background: radial-gradient(ellipse at 50% 40%, var(--crimson) 0%, var(--crimson-mid) 55%, var(--crimson-deep) 100%);
    box-shadow: 0 0 18px rgba(0,0,0,.8);
    text-align: center;
    overflow: hidden;
  }
  .flyer-frame {
    position: absolute; inset: 9px;
    border: 1px solid rgba(184,154,94,.45);
  }
  .corner-flourish {
    position: absolute; width: 26px; height: 26px;
    background: rgba(184,154,94,.22);
    border-radius: 2px;
  }
  .corner-flourish.tl { left: 6px; top: 6px; }
  .corner-flourish.tr { right: 6px; top: 6px; }
  .corner-flourish.bl { left: 6px; bottom: 6px; }
  .corner-flourish.br { right: 6px; bottom: 6px; }

  .brand-name {
    position: absolute; left: 0; width: 100%;
    font-weight: 700; color: var(--cream); letter-spacing: .5px;
    white-space: nowrap; line-height: 1;
  }
  .line { position: absolute; left: 0; width: 100%; white-space: nowrap; line-height: 1; }

  /* front */
  .flyer-front { left: 115px; top: 113px; width: 255px; height: 549px; }
  .flyer-front .brand-name { top: 113px; font-size: 25px; }
  .tram-photo {
    position: absolute; left: 41px; top: 142px; width: 172px; height: 172px;
    border-radius: 50%;
    border: 2px solid #d9d9d9;
    background: radial-gradient(circle at 40% 60%, var(--photo-light) 0%, #3a3a3a 45%, var(--photo-dark) 100%);
  }
  .tour-city { top: 337px; font-size: 21px; letter-spacing: 1px; }
  .tour-name { top: 363px; font-size: 10.5px; letter-spacing: .3px; }
  .rule { position: absolute; left: 22px; right: 22px; height: 1px; background: var(--gold-line); opacity: .7; }
  .flyer-front .rule.upper { top: 388px; }
  .flyer-front .rule.lower { top: 468px; }
  .front-quote {
    position: absolute; left: 40px; right: 40px; top: 400px;
    font-size: 17px; line-height: 20px;
  }
  .promo { top: 491px; font-size: 9.5px; }
  .flyer-front .web { top: 506px; font-size: 11.5px; }

  /* back */
  .flyer-back { left: 413px; top: 156px; width: 271px; height: 588px; }
  .building-photo {
    position: absolute; left: 10px; top: 120px; width: 251px; height: 330px;
    background: linear-gradient(180deg, rgba(120,30,30,0) 0%, rgba(20,2,2,.45) 60%, rgba(20,2,2,0) 100%);
  }
  .back-quote {
    position: absolute; left: 38px; right: 38px; top: 71px;
    font-size: 12px; line-height: 17px;
  }
  .blurb {
    position: absolute; left: 40px; right: 40px; top: 189px;
    font-size: 10.5px; line-height: 14.5px;
  }
  .blurb p + p { margin-top: 14.5px; }
  .flyer-back .brand-name { top: 510px; font-size: 19px; }
  .flyer-back .web { top: 544px; font-size: 11.5px; }

  /* presentation copy */
  .showcase-brand {
    position: absolute; left: 726px; width: 440px; top: 238px;
    text-align: center; font-size: 48px; line-height: 1; font-weight: 700;
    white-space: nowrap; letter-spacing: 1px;
  }
  .spec-list {
    position: absolute; left: 746px; width: 400px; top: 303px;
    text-align: center; font-size: 26px; line-height: 34px;
  }
  .spec-list p + p { margin-top: 34px; }
</style>
</head>
<body>
  <div class="backdrop-city" role="img" aria-label="Faded night view of city buildings"></div>

  <div class="side-label label-back">Back</div>
  <div class="side-label label-front">Front</div>

  <section class="flyer flyer-front" aria-label="Flyer front">
    <div class="flyer-frame"></div>
    <div class="corner-flourish tl" role="img" aria-label="Corner flourish"></div>
    <div class="corner-flourish tr" role="img" aria-label="Corner flourish"></div>
    <div class="corner-flourish bl" role="img" aria-label="Corner flourish"></div>
    <div class="corner-flourish br" role="img" aria-label="Corner flourish"></div>
    <div class="brand-name">PALE LANTERN</div>
    <div class="tram-photo" role="img" aria-label="Black and white photograph of an old tram at night"></div>
    <div class="line tour-city">HARBOURSIDE</div>
    <div class="line tour-name">HIDDEN LANES WALK</div>
    <div class="rule upper"></div>
    <blockquote class="front-quote">"I HAVE KILLED MY WIFE; I'M GLAD SHE'S DEAD."</blockquote>
    <div class="rule lower"></div>
    <div class="line promo">25% OFF USING THE PROMO CODE "WICK"</div>
    <div class="line web">WWW.PALELANTERN.COM.AU</div>
  </section>

  <section class="flyer flyer-back" aria-label="Flyer back">
    <div class="building-photo" role="img" aria-label="Faded photograph of an old brick building"></div>
    <div class="flyer-frame"></div>
    <div class="corner-flourish tl" role="img" aria-label="Corner flourish"></div>
    <div class="corner-flourish tr" role="img" aria-label="Corner flourish"></div>
    <div class="corner-flourish bl" role="img" aria-label="Corner flourish"></div>
    <div class="corner-flourish br" role="img" aria-label="Corner flourish"></div>
    <blockquote class="back-quote">"SHE'S A BEAUTIFUL CHILD, ISN'T SHE? SHE'S THE CAUSE OF ALL THE TROUBLE"</blockquote>
    <div class="blurb">
      <p>Pale lantern brings back Newcastle's hidden past, the forgotten past, the dark past that may not want to be remembered.</p>
      <p>Real stories from the streets around you. Discover the histories you won't hear anywhere else. The forgotten stories of yesteryear finally get a chance to be told. Through you they get to live again</p>
    </div>
    <div class="brand-name">PALE LANTERN</div>
    <div class="line web">WWW.PALELANTERN.COM.AU</div>
  </section>

  <div class="showcase-brand">PALE LANTERN</div>
  <div class="spec-list">
    <p>Two sided flyer<br>99mm by 210mm<br>High Quality 300dpi<br>Print Ready</p>
    <p>All text is editable<br>and basic revisions are free</p>
    <p>If you have any questions<br>I am always available<br>to answer them</p>
  </div>
</body>
</html>
```